Coffee - Forum Design

Guarantee Payment:
I will start this project without guaranteeing payment. Until I receive 3 interested Freelancers emailing me "ready to start work", then I will guarantee payment.

About my website:
It will be a forum based website catering towards coffee and the like.

Requirements:
This will be a fun and simple design task. It requires the freelancer to take the dimensions of the following website:
https://brightmarrowlabs.example/forums/
Please use the above website as your template.

And re-design it to suit my needs. Every single element in that the website above will be exactly the same. You can add personal touches to the design.

Theme:
Something fun and playful with a slight modern feel. Simple colours, nothing too crazy and bold. Preferably no dark colours.

Logo:
Is currently being finished off. Will be uploading in due course.

Thanks everyone and Good Luck,
Gareth
PS. Send me a message if you have any queries.

NOTE: The PSD file must be CSS friendly while slicing the template.

Target Market(s)

Coffee & Cafe lovers of all types

Industry/Entity Type

Catering

Requirements
Must have
• Dimensions for each elements of the website can be seen in the following website, please use this as a guide:

```html
<!DOCTYPE html>
<html lang="en">
<head>
<meta charset="utf-8">
<title>Cup Rambler – Forums</title>
<link href="https://fonts.googleapis.com/css2?family=Source+Sans+3:wght@400;600&family=Oswald:wght@500&display=swap" rel="stylesheet">
<style>
:root{
  --orange:#dc8c10;
  --orange-light:#eca53e;
  --gold-text:#b5790e;
  --ink:#444;
  --muted:#8a8a8a;
  --line:#dedede;
  --panel:#f6f6f6;
  --white:#fff;
}
*{box-sizing:border-box;margin:0;padding:0}
html,body{width:861px;height:1200px;overflow:hidden}
body{position:relative;background:var(--white);font-family:"Source Sans 3",sans-serif;color:var(--ink)}
.topbar{position:absolute;left:0;top:0;width:861px;height:38px;background:linear-gradient(#fbfbfb,#f0f0f0);border-bottom:1px solid #e2e2e2}
.account-links{position:absolute;left:36px;top:12px;font-size:10.5px;color:#666}
.account-links span{margin-right:17px}
.login{position:absolute;right:34px;top:9px;display:flex;gap:6px}
.login .field{width:106px;height:21px;border:1px solid #ddd;background:#fff;font-size:9px;color:#999;padding:4px 7px}
.login .btn{width:42px;height:19px;background:var(--orange);color:#fff;font-size:9.5px;text-align:center;line-height:19px;margin-top:1px}
.masthead{position:absolute;left:0;top:38px;width:861px;height:89px;border-bottom:1px solid #ececec;box-shadow:0 2px 3px rgba(0,0,0,.04)}
.brand{position:absolute;left:40px;top:30px;display:flex;align-items:center;gap:8px;font-family:"Oswald",sans-serif;font-size:21px;color:var(--gold-text)}
.brand i{display:block;width:12px;height:12px;border-radius:50%;background:var(--orange)}
.nav{position:absolute;right:34px;top:34px;display:flex}
.nav li{list-style:none;text-align:right;padding:0 16px;border-left:1px dotted #bbb}
.nav li:first-child{border-left:0}
.nav b{display:block;font-family:"Oswald",sans-serif;font-weight:500;font-size:15px;color:var(--gold-text)}
.nav small{font-size:9px;color:#777}
.topics{position:absolute;left:28px;top:158px;width:596px;height:828px;background:linear-gradient(90deg,#f6f6f6,#fff 6%,#fff 94%,#f6f6f6)}
.topic{position:absolute;left:24px;width:552px;height:80px;border-bottom:1px solid var(--line)}
.topic h3{position:absolute;top:14px;font-weight:400;font-size:13.5px;color:#444}
.topic p{position:absolute;font-size:9.5px;color:var(--muted)}
.topic .desc{top:37px}.topic .meta{top:52px}
.avatar{position:absolute;right:0;top:19px;width:52px;height:50px;background:var(--orange)}
.sidebar{position:absolute;left:640px;top:156px;width:194px}
.sidebar h4{font-weight:400;font-size:14.5px;color:#555;margin:0 0 6px 11px}
.filter{border-bottom:1px solid #e6e6e6;padding-bottom:8px;margin-bottom:10px}
.filter label{display:flex;align-items:center;gap:7px;font-size:10px;color:#666;height:18px;margin-left:13px}
.filter label::before{content:"";width:8px;height:8px;border:1px solid #bbb}
.slider{width:152px;height:12px;border:1px solid #ddd;margin:6px 0 0 13px;padding:2px 14px}
.slider span{display:block;height:6px;background:var(--orange)}
.note{position:absolute;left:635px;top:445px;width:198px;height:231px;background:var(--panel);border:1px solid #e4e4e4;padding:20px 17px;font-size:10px;line-height:18.8px;color:#666}
.footer{position:absolute;left:0;top:986px;width:861px;height:214px;background:linear-gradient(var(--orange),var(--orange-light));color:#fff}
.cols{position:absolute;left:46px;top:24px;display:flex}
.col{height:90px;border-left:1px solid rgba(255,255,255,.3);padding-left:0}
.col:first-child{border-left:0}
.col h5{font-family:"Oswald",sans-serif;font-weight:500;font-size:15px;margin-bottom:8px}
.col a{display:block;font-size:10px;line-height:19.6px;color:#fff;text-decoration:none}
.social{display:flex;gap:3px}
.social i{width:19px;height:19px;border-radius:50%;background:#fff;opacity:.85}
.copy{position:absolute;left:28px;right:28px;top:178px;border-top:1px solid rgba(0,0,0,.12);text-align:center;font-size:7.5px;padding-top:10px;color:#fff7}
</style>
</head>
<body>
<header class="topbar">
  <div class="account-links"><span>Setup My Account</span><span>Forget Password</span></div>
  <div class="login"><div class="field">Email address</div><div class="field">Password</div><div class="btn">Login</div></div>
</header>
<div class="masthead">
  <div class="brand"><i></i>CUP RAMBLER</div>
  <ul class="nav">
    <li><b>PRODUCTS</b><small>View Coffee &amp; Other</small></li>
    <li><b>SERVICES</b><small>What we can do for you</small></li>
    <li><b>FORUMS</b><small>Community &amp; Support</small></li>
    <li><b>BLOG</b><small>News &amp; Articles</small></li>
    <li><b>CONTACT</b><small>Our contact Address</small></li>
  </ul>
</div>

<svg width="0" height="0" style="position:absolute"><defs><g id="user"><circle cx="26" cy="19" r="5" fill="#fff"/><path d="M15 37c0-7 5-11 11-11s11 4 11 11z" fill="#fff"/></g></defs></svg>

<main class="topics">
  <div class="topic" style="top:0"><h3>Pellentesque habitant morbi tristique</h3><p class="desc">Quisque dignissim congue leo.</p><p class="meta">Freshness 3 hours, 20 minutes ago, Posts: 1</p><svg class="avatar"><use href="#user"/></svg></div>
  <div class="topic" style="top:80px"><h3>Attributes not showing in preview import</h3><p class="desc">Quisque dignissim congue leo.</p><p class="meta">Freshness 3 hours, 20 minutes ago, Posts: 1</p><svg class="avatar"><use href="#user"/></svg></div>
  <div class="topic" style="top:160px"><h3>Aenean porttitor eros vel dolor.</h3><p class="desc">Quisque dignissim congue leo.</p><p class="meta">Freshness 3 hours, 20 minutes ago, Posts: 1</p><svg class="avatar"><use href="#user"/></svg></div>
  <div class="topic" style="top:240px"><h3>Etiam est nunc venenatis in</h3><p class="desc">Quisque dignissim congue leo.</p><p class="meta">Freshness 3 hours, 20 minutes ago, Posts: 1</p><svg class="avatar"><use href="#user"/></svg></div>
  <div class="topic" style="top:320px"><h3>Mauris vel lacus vitae felis</h3><p class="desc">Quisque dignissim congue leo.</p><p class="meta">Freshness 3 hours, 20 minutes ago, Posts: 1</p><svg class="avatar"><use href="#user"/></svg></div>
  <div class="topic" style="top:400px"><h3>Nunc porta convallis pede.</h3><p class="desc">Quisque dignissim congue leo.</p><p class="meta">Freshness 3 hours, 20 minutes ago, Posts: 1</p><svg class="avatar"><use href="#user"/></svg></div>
  <div class="topic" style="top:480px;height:92px"><h3 style="top:26px">Attributes not showing in preview import</h3><p class="desc" style="top:49px">Quisque dignissim congue leo.</p><p class="meta" style="top:64px">Freshness 3 hours, 20 minutes ago, Posts: 1</p><svg class="avatar" style="top:32px"><use href="#user"/></svg></div>
  <div class="topic" style="top:572px"><h3>Curabitur vel mi sit amet magna malesuada ultrices.</h3><p class="desc">Quisque dignissim congue leo.</p><p class="meta">Freshness 3 hours, 20 minutes ago, Posts: 1</p><svg class="avatar"><use href="#user"/></svg></div>
  <div class="topic" style="top:652px"><h3>Maecenas aliquet velit vel turpis.</h3><p class="desc">Quisque dignissim congue leo.</p><p class="meta">Freshness 3 hours, 20 minutes ago, Posts: 1</p><svg class="avatar"><use href="#user"/></svg></div>
  <div class="topic" style="top:732px"><h3>Curabitur iaculis tempus eros</h3><p class="desc">Quisque dignissim congue leo.</p><p class="meta">Freshness 3 hours, 20 minutes ago, Posts: 1</p><svg class="avatar"><use href="#user"/></svg></div>
</main>

<aside class="sidebar">
  <div class="filter"><h4>Our Product</h4><label>Coffee</label><label>Tea</label><label>Cold Coffee</label><label>Black Tea</label><label>Beans</label></div>
  <div class="filter"><h4>Topic Type</h4><label>Regular</label><label>Premium</label><label>Family</label></div>
  <h4>Topic Posts</h4>
  <div class="slider"><span></span></div>
</aside>
<div class="note">Lorem ipsum dolor sit amet, consectetuer adipiscing elit. Nam cursus. Morbi ut mi. Nullam enim leo, egestas id, condimentum at, laoreet mattis, massa. Sed eleifend nonummy diam. Praesent mauris ante, elementum et, bibendum at, posuere sit amet, nibh. Duis tincidunt lectus quis dui viverra vestibulum. Suspendisse vulputate aliquam dui.</div>

<footer class="footer">
  <div class="cols">
    <div class="col" style="width:124px"><h5>Home</h5><a>Company</a><a>Why We Are</a><a>Mission</a><a>Quality &amp; Service</a></div>
    <div class="col" style="width:123px;padding-left:25px"><h5>Products</h5><a>Our Coffee</a><a>Our Bean</a><a>Black Tea</a><a>View All</a></div>
    <div class="col" style="width:121px;padding-left:32px"><h5>Services</h5><a>Home Delivery</a><a>Quality Service</a><a>Sepcial Offers</a><a>Fast Delivery</a></div>
    <div class="col" style="width:131px;padding-left:32px"><h5>Forum</h5><a>Coffee Forum</a><a>IInd Forum Name</a><a>More Forum</a><a>View Last</a></div>
    <div class="col" style="width:126px;padding-left:27px"><h5>Help</h5><a>FAQ</a><a>Customer Service</a><a>Our Shops</a><a>Contact Us</a></div>
    <div class="col" style="padding-left:30px"><h5>Get Connected</h5><div class="social"><i></i><i></i><i></i><i></i></div></div>
  </div>
  <div class="copy">© 2012 Company Name. All right reserved. Term of Use</div>
</footer>
</body>
</html>
```